Business Card Design

We need a business card design for a new dental practice in Brisbane. I'd like the basic details and logo on one side and appointment schedule on the other side. It is based in CBD office area and would prefer a professional and modern design.
Target Market(s)
20-60 years old office workers and residents with high education levels
Industry/Entity Type
Dental
Contact Information for Business Card
Harbourlight Dental
Dr Marcus Lindqvist
Principal Dentist
07 3194 6627
admin@harbourlightdentistry.example.au
www.harbourlightdentistry.example.au
S27, Level 3, Ferndale North Tower, 318 Gorrick St, Alderwood Heights, QLD 4118

```html
<!DOCTYPE html>
<html lang="en">
<head>
<meta charset="utf-8">
<title>Harbourlight Dental – Business Card</title>
<link rel="stylesheet" href="https://fonts.googleapis.com/css2?family=Quicksand:wght@500;700&display=swap">
<style>
  :root {
    --backdrop: #2b2e31;
    --card-navy: #1f4a97;
    --card-navy-light: #2c62b4;
    --band-cyan: #5fe3ee;
    --text-white: #ffffff;
    --text-soft: #d8e6f7;
    --card-white: #ffffff;
    --card-white-shade: #e9ecef;
    --brand-ink: #1d2a33;
    --brand-dot: #3fb7e0;
  }
  * { box-sizing: border-box; margin: 0; padding: 0; }
  html, body {
    width: 1200px; height: 900px; overflow: hidden;
    background: var(--backdrop);
    font-family: "Quicksand", "Helvetica Neue", Arial, sans-serif;
  }
  .stage {
    position: relative; width: 1200px; height: 900px;
    display: flex; flex-direction: column; align-items: center; justify-content: center; gap: 44px;
  }
  .card {
    position: relative; width: 580px; height: 332px;
    box-shadow: 0 10px 26px rgba(0,0,0,0.45);
    overflow: hidden;
  }
  /* Contact side */
  .card--contact {
    background: var(--band-cyan);
    padding: 24px 0;
  }
  .contact-panel {
    position: relative; height: 100%;
    background: linear-gradient(100deg, var(--card-navy) 0%, var(--card-navy) 55%, var(--card-navy-light) 100%);
    color: var(--text-white);
  }
  .dentist {
    position: absolute; top: 16px; right: 26px; text-align: right;
  }
  .dentist__name { font-weight: 700; font-size: 19px; letter-spacing: 0.2px; }
  .dentist__role { font-weight: 500; font-size: 11.5px; color: var(--text-soft); margin-top: 1px; }
  .details {
    position: absolute; left: 34px; bottom: 18px;
  }
  .details__practice { font-weight: 700; font-size: 17px; margin-bottom: 8px; }
  .details__list { list-style: none; }
  .details__item {
    display: flex; align-items: center; gap: 9px;
    font-weight: 500; font-size: 13.5px; line-height: 19px;
  }
  .details__item svg { width: 15px; height: 15px; flex: none; }
  .details__address {
    display: flex; gap: 9px; margin-top: 10px;
    font-weight: 500; font-size: 13.5px; line-height: 18px;
  }
  .details__address svg { width: 15px; height: 15px; flex: none; margin-top: 2px; }
  /* Brand side */
  .card--brand {
    background: linear-gradient(115deg, var(--card-white) 0%, var(--card-white) 45%, var(--card-white-shade) 100%);
    display: flex; align-items: center; justify-content: center; gap: 16px;
  }
  .brand__dot {
    width: 30px; height: 30px; border-radius: 50%; background: var(--brand-dot);
  }
  .brand__name {
    font-weight: 700; font-size: 46px; color: var(--brand-ink); letter-spacing: 0.3px;
  }
</style>
</head>
<body>
<main class="stage">
  <section class="card card--contact" aria-label="Business card contact side">
    <div class="contact-panel">
      <div class="dentist">
        <p class="dentist__name">Dr Marcus Lindqvist</p>
        <p class="dentist__role">Principal Dentist</p>
      </div>
      <div class="details">
        <p class="details__practice">Harbourlight Dental</p>
        <ul class="details__list">
          <li class="details__item">
            <svg viewBox="0 0 16 16" aria-hidden="true"><path d="M2 6c0-2 3-3.5 6-3.5S14 4 14 6l-2.5 1L10.5 5h-5L4.5 7z M4 8h8l1 5H3z" fill="#fff"/><circle cx="8" cy="10.5" r="1.4" fill="#1f4a97"/></svg>
            07 3194 6627
          </li>
          <li class="details__item">
            <svg viewBox="0 0 16 16" aria-hidden="true"><rect x="1.5" y="3.5" width="13" height="9" fill="none" stroke="#fff" stroke-width="1.4"/><path d="M1.5 3.5 8 9l6.5-5.5" fill="none" stroke="#fff" stroke-width="1.4"/></svg>
            admin@harbourlightdentistry.example.au
          </li>
          <li class="details__item">
            <svg viewBox="0 0 16 16" aria-hidden="true"><g fill="none" stroke="#fff" stroke-width="1.2"><circle cx="8" cy="8" r="6.3"/><ellipse cx="8" cy="8" rx="2.8" ry="6.3"/><path d="M1.7 8h12.6M2.8 4.8h10.4M2.8 11.2h10.4"/></g></svg>
            www.harbourlightdentistry.example.au
          </li>
        </ul>
        <div class="details__address">
          <svg viewBox="0 0 16 16" aria-hidden="true"><path d="M8 1.8 1 8h2v6h4v-4h2v4h4V8h2z" fill="#fff"/></svg>
          <address style="font-style:normal">S27, Level 3<br>Ferndale North Tower<br>318 Gorrick St<br>Alderwood Heights, QLD 4118</address>
        </div>
      </div>
    </div>
  </section>

  <section class="card card--brand" aria-label="Business card brand side">
    <span class="brand__dot" aria-hidden="true"></span>
    <h1 class="brand__name">Harbourlight Dental</h1>
  </section>
</main>
</body>
</html>
```